3 x Webpage Homepage Banner for New Scrap Metal Company website

New website (currently under construction) for a scrap metal recycling company require 3 home page banner that give visitor have a sense of confident and relevance in the company. Feeling good about the products and value.

I have attached here a file name "website home page" to show the currently general idea of the design of the webpage. Two more file "Regular Login 1" and "Regular Login 2" to show the currently "looks" when a user visit the page. The current banner is a dummy.

One of the file titled "Company Image" is the picture of our company which I would also like to have it in one of the banner.

```html
<!DOCTYPE html>
<html lang="en">
<head>
<meta charset="utf-8">
<title>Kian Heng Recycling</title>
<link href="https://fonts.googleapis.com/css2?family=Rubik:wght@400;500;700;800&family=Poppins:wght@400;500;600&display=swap" rel="stylesheet">
<style>
:root{
  --gold:#d4a12b;
  --gold-dark:#b8861c;
  --ink:#2f2f2f;
  --muted:#6b6b6b;
  --dark:#3b3b3b;
  --darker:#2c2c2c;
  --light:#f1f1f1;
  --white:#ffffff;
  --red:#c8242b;
}
*{box-sizing:border-box;margin:0;padding:0}
html,body{width:1200px;height:4176px;overflow:hidden}
body{font-family:"Poppins",sans-serif;color:var(--ink);background:var(--white);position:relative}
h1,h2,h3,.display{font-family:"Rubik",sans-serif}
.abs{position:absolute}

/* header */
.header{position:absolute;left:0;top:0;width:1200px;height:148px;background:var(--white)}
.brand{position:absolute;left:88px;top:36px;display:flex;align-items:center;gap:12px}
.brand-square{width:40px;height:40px;background:var(--gold)}
.brand-name{font-family:"Rubik",sans-serif;font-weight:700;font-size:22px;color:var(--gold);letter-spacing:.5px}
.contact-item{position:absolute;top:36px;display:flex;gap:10px;align-items:center;font-size:13px;line-height:1.3}
.contact-item b{display:block;font-weight:600;font-size:13px}
.contact-item span{color:var(--muted);font-size:12px}
.btn-login{position:absolute;left:1012px;top:38px;width:100px;height:36px;background:var(--gold);color:#fff;font-size:12px;font-weight:600;display:flex;align-items:center;justify-content:center;gap:6px}
.nav{position:absolute;left:88px;top:106px;display:flex;gap:44px;font-size:13px;font-weight:600;letter-spacing:.5px}
.nav a{color:var(--ink);text-decoration:none;padding-bottom:12px}
.nav a.active{border-bottom:3px solid var(--gold)}

/* hero */
.hero{position:absolute;left:0;top:148px;width:1200px;height:752px;overflow:hidden}
.hero-photo{position:absolute;inset:0;background:linear-gradient(100deg,#2a3550 0%,#3e5e95 35%,#6f95cf 60%,#a9c4e6 100%)}
.hero-shade{position:absolute;inset:0;background:linear-gradient(90deg,rgba(20,28,45,.75),rgba(20,28,45,.25) 55%,rgba(0,0,0,0))}
.hero-cut{position:absolute;right:0;bottom:0}
.hero h1{position:absolute;left:88px;top:190px;color:#fff;font-size:76px;font-weight:800;line-height:1}
.hero h2{position:absolute;left:88px;top:272px;color:#fff;font-size:34px;font-weight:700}
.hero p{position:absolute;left:88px;top:328px;width:380px;color:#e8ecf3;font-size:13px;line-height:1.55}
.btn-gold{background:var(--gold);color:#fff;font-size:12px;font-weight:600;display:flex;align-items:center;justify-content:center;letter-spacing:.5px}
.hero .btn-gold{position:absolute;left:88px;top:430px;width:150px;height:44px}
.hero-arrow{position:absolute;top:660px;width:56px;height:56px;border-radius:50%;display:flex;align-items:center;justify-content:center}
.hero-dots{position:absolute;left:232px;top:684px;display:flex;gap:8px}
.hero-dots i{width:8px;height:8px;border-radius:50%;background:rgba(255,255,255,.5);display:block}
.hero-dots i.on{background:#fff}

/* about */
.about-frame{position:absolute;left:112px;top:930px;width:406px;height:400px;border:10px solid #f3ead4}
.about-photo{position:absolute;left:88px;top:962px;width:386px;height:392px;background:radial-gradient(circle at 60% 70%,#f7b53a 0%,#c66a1a 25%,#3a2a22 60%,#1c1a1c 100%)}
.about-title{position:absolute;left:632px;top:980px}
.about-title h2{font-size:80px;font-weight:800;color:var(--gold);line-height:1}
.about-title h3{font-size:30px;font-weight:700;color:var(--ink);margin-top:6px}
.about-text{position:absolute;left:632px;top:1110px;width:480px;font-size:13px;line-height:1.65;color:var(--muted)}
.about-text p+p{margin-top:14px}
.btn-outline{position:absolute;left:632px;top:1336px;width:120px;height:40px;border:2px solid var(--ink);font-size:12px;font-weight:600;display:flex;align-items:center;justify-content:center}

/* section titles */
.sec-title{position:absolute;left:0;width:1200px;text-align:center}
.sec-title h2{font-size:44px;font-weight:700;color:var(--ink)}
.sec-title p{font-size:13px;color:var(--muted);line-height:1.6;width:680px;margin:10px auto 0}

/* service cards */
.svc{position:absolute;top:1700px;width:316px;height:364px;background:#fff;box-shadow:0 6px 22px rgba(0,0,0,.12)}
.svc-photo{height:200px;clip-path:polygon(0 0,100% 0,100% 78%,0 100%)}
.svc h3{font-size:20px;font-weight:600;margin:22px 24px 6px}
.svc p{font-size:12px;color:var(--muted);margin:0 24px;line-height:1.5}
.svc .link{position:absolute;right:24px;bottom:26px;font-size:11px;font-weight:600;color:var(--gold)}

/* why */
.why{position:absolute;left:0;top:2172px;width:1200px;height:590px}
.why-title{position:absolute;top:72px;left:0;width:1200px;text-align:center;color:#fff;font-size:44px;font-weight:700}
.why-mark{position:absolute;left:440px;top:168px;width:320px;height:332px;background:#fff;border:8px solid #f2e2b6;display:flex;align-items:center;justify-content:center;flex-direction:column;gap:14px}
.why-mark .sq{width:60px;height:60px;background:var(--gold)}
.why-mark span{font-family:"Rubik",sans-serif;font-weight:700;color:var(--gold);font-size:26px}
.feat{position:absolute;width:300px;color:#fff}
.feat h4{font-family:"Rubik",sans-serif;font-size:20px;font-weight:600}
.feat p{font-size:12px;line-height:1.45;color:#fbf1d8;margin-top:4px}
.feat.left{text-align:right;left:50px}
.feat.right{left:860px}
.feat-icon{position:absolute;top:4px}
.feat.left .feat-icon{left:316px}
.feat.right .feat-icon{left:-46px}

/* products */
.prod{position:absolute;top:2968px;width:300px;height:470px;background:#fff;box-shadow:0 6px 22px rgba(0,0,0,.12)}
.prod-photo{height:300px}
.prod .cat{text-align:right;font-size:11px;color:var(--muted);margin:22px 24px 2px}
.prod h3{text-align:right;font-size:20px;font-weight:600;margin:0 24px}
.prod .price{text-align:right;font-size:14px;color:var(--gold);font-weight:600;margin:2px 24px}
.cart{position:absolute;left:24px;bottom:32px;width:44px;height:44px;background:var(--red);display:flex;align-items:center;justify-content:center}
.pager{position:absolute;left:1044px;width:70px;height:40px;background:#fff;box-shadow:0 3px 12px rgba(0,0,0,.15);font-size:11px;font-weight:600;display:flex;align-items:center;justify-content:center}

/* cta */
.cta{position:absolute;left:392px;top:3556px;width:748px;height:150px;background:var(--light);text-align:center}
.cta h2{font-size:34px;font-weight:700;color:#4a4a4a;margin-top:32px}
.cta p{font-size:13px;color:var(--muted);margin-top:6px}
.cta-btn{position:absolute;left:388px;top:3690px;width:424px;height:88px;font-size:18px;gap:14px;z-index:2}

/* footer */
.footer{position:absolute;left:0;top:3700px;width:1200px;height:420px;background:var(--dark);color:#d9d9d9}
.footer .brand{left:88px;top:232px}
.socials{position:absolute;left:140px;top:292px;display:flex;gap:12px}
.socials i{width:28px;height:28px;border-radius:50%;border:1px solid #888;display:block}
.fcol{position:absolute;top:150px;font-size:12px;line-height:2.1}
.fcol h4{font-family:"Rubik",sans-serif;font-size:16px;font-weight:600;color:#fff;margin-bottom:8px;line-height:1.3}
.fcol .row{display:flex;gap:10px;line-height:1.45;margin-bottom:12px}
.fcol .row b{display:block;color:#fff;font-weight:600}
.footer-bar{position:absolute;left:0;top:4120px;width:1200px;height:56px;background:var(--darker);color:#bbb;font-size:12px;text-align:center;line-height:56px}
.to-top{position:absolute;left:1140px;top:4132px;width:32px;height:32px;border-radius:50%;background:var(--gold)}
</style>
</head>
<body>

<header class="header">
  <div class="brand"><div class="brand-square"></div><div class="brand-name">KIAN HENG</div></div>
  <div class="contact-item" style="left:640px">
    <svg width="24" height="24" viewBox="0 0 24 24"><path d="M6 3l4 4-2 3c1 3 3 5 6 6l3-2 4 4-3 3C9 21 3 15 3 6z" fill="var(--ink)"/></svg>
    <div><b>Call Us</b><span>+(65) 6000 1234</span></div>
  </div>
  <div class="contact-item" style="left:840px">
    <svg width="24" height="24" viewBox="0 0 24 24"><path d="M3 5h3l3 10h10l2-7H8" fill="none" stroke="var(--ink)" stroke-width="2"/><circle cx="10" cy="19" r="1.6" fill="var(--ink)"/><circle cx="18" cy="19" r="1.6" fill="var(--ink)"/></svg>
    <div><b>My Cart</b><span>0 Items – SGD 0.00</span></div>
  </div>
  <div class="btn-login">
    <svg width="12" height="12" viewBox="0 0 12 12"><circle cx="6" cy="4" r="2.5" fill="#fff"/><path d="M1 12c0-3 2-5 5-5s5 2 5 5z" fill="#fff"/></svg>LOGIN
  </div>
  <nav class="nav">
    <a class="active">HOME</a><a>ABOUT US</a><a>PRODUCTS</a><a>OUR SERVICES</a><a>INVESTORS</a><a>CONTACT US</a>
  </nav>
</header>

<section class="hero">
  <div class="hero-photo" role="img" aria-label="Photo of the company's recycling warehouse building under a blue sky"></div>
  <div class="hero-shade"></div>
  <svg class="hero-cut" width="420" height="400" viewBox="0 0 420 400"><polygon points="420,0 420,400 0,400" fill="#fff"/></svg>
  <h1>Recycling</h1>
  <h2>Industrial Metal Scraps</h2>
  <p>Procurement, processing, recycling and trading of all ferrous and non-ferrous metals, industrial scraps and other recyclables.</p>
  <div class="btn-gold">OUR SERVICES</div>
  <div class="hero-arrow" style="left:88px;background:rgba(255,255,255,.25)">
    <svg width="18" height="14" viewBox="0 0 18 14"><path d="M7 1L1 7l6 6M1 7h16" fill="none" stroke="#fff" stroke-width="2"/></svg>
  </div>
  <div class="hero-arrow" style="left:156px;background:#fff">
    <svg width="18" height="14" viewBox="0 0 18 14"><path d="M11 1l6 6-6 6M17 7H1" fill="none" stroke="var(--ink)" stroke-width="2"/></svg>
  </div>
  <div class="hero-dots"><i class="on"></i><i></i><i></i></div>
</section>

<section>
  <div class="about-frame"></div>
  <div class="about-photo" role="img" aria-label="Photo of a worker cutting metal with sparks flying"></div>
  <div class="about-title"><h2>About</h2><h3>Scrap Metal for Recycling</h3></div>
  <div class="about-text">
    <p>Kian Heng Recycling primary activities are the procurement, processing, recycling and trading of all ferrous and non-ferrous scrap metals, industrial scraps and other recyclables.</p>
    <p>We provide full-service ferrous and non-ferrous metal recycle and processing. Recognised as an industry leader in metal recycling, our team of experienced staff and trader understand the intricacies of scrap metal recycling.</p>
  </div>
  <div class="btn-outline">ABOUT US</div>
</section>

<section>
  <div class="sec-title" style="top:1560px">
    <h2>Our Services</h2>
    <p>Services have always been our priority to ensure continuous customer satisfaction and will do our utmost to meet our customers' requirements. Our prices are review daily to ensure that our company.</p>
  </div>
  <div class="svc" style="left:88px">
    <div class="svc-photo" role="img" aria-label="Photo of stacked steel sheets" style="background:linear-gradient(135deg,#e6e6e6,#9b9b9b 60%,#5b5b5b)"></div>
    <h3>For Individual</h3><p>Kian Heng Recycling provides excellent service &amp; very.</p><div class="link">VIEW ALL PRODUCTS</div>
  </div>
  <div class="svc" style="left:442px">
    <div class="svc-photo" role="img" aria-label="Photo of coiled copper wire" style="background:linear-gradient(135deg,#f3b07a,#c2602a 55%,#6a2a14)"></div>
    <h3>For Corporate</h3><p>Kian Heng Recycling provides excellent service &amp; very.</p><div class="link">VIEW ALL PRODUCTS</div>
  </div>
  <div class="svc" style="left:796px">
    <div class="svc-photo" role="img" aria-label="Photo of steel angle bars" style="background:linear-gradient(135deg,#dcdcdc,#8d8d8d 55%,#3d3d3d)"></div>
    <h3>For International</h3><p>Kian Heng Recycling provides excellent service &amp; very.</p><div class="link">VIEW ALL PRODUCTS</div>
  </div>
</section>

<section class="why">
  <svg class="abs" width="1200" height="590" viewBox="0 0 1200 590" style="left:0;top:0"><polygon points="0,0 1040,0 1200,70 1200,590 140,590 0,540" fill="var(--gold)"/></svg>
  <h2 class="why-title">Why Choose Us</h2>
  <div class="why-mark"><div class="sq"></div><span>KIAN HENG</span></div>

  <div class="feat left" style="top:176px"><h4>Scrap Yard</h4><p>Fully equipped facility to handle all your scrap metal, efficient.</p>
    <svg class="feat-icon" width="34" height="34" viewBox="0 0 34 34"><path d="M3 26h28M6 26V12l8-6 8 6v14M24 26V16h6v10" fill="none" stroke="#fff" stroke-width="2.2"/></svg></div>
  <div class="feat left" style="top:290px"><h4>Collection</h4><p>Free collection to provide onsite collection services at ease.</p>
    <svg class="feat-icon" width="34" height="34" viewBox="0 0 34 34"><path d="M2 9h19v14H2zM21 14h6l5 5v4H21z" fill="none" stroke="#fff" stroke-width="2.2"/><circle cx="8" cy="25" r="3" fill="#fff"/><circle cx="26" cy="25" r="3" fill="#fff"/></svg></div>
  <div class="feat left" style="top:400px"><h4>Highest Value</h4><p>Daily price monitoring, offer good rewards of scrap you own.</p>
    <svg class="feat-icon" width="34" height="34" viewBox="0 0 34 34"><circle cx="17" cy="17" r="13" fill="none" stroke="#fff" stroke-width="2.2"/><path d="M17 9v16M21 12h-6a3 3 0 000 6h4a3 3 0 010 6h-6" fill="none" stroke="#fff" stroke-width="2"/></svg></div>

  <div class="feat right" style="top:176px"><h4>Authorized</h4><p>We have certification and licensed you require for all your.</p>
    <svg class="feat-icon" width="34" height="34" viewBox="0 0 34 34"><path d="M17 3l12 5v8c0 8-6 13-12 15C11 29 5 24 5 16V8z" fill="none" stroke="#fff" stroke-width="2.2"/><path d="M11 17l4 4 8-8" fill="none" stroke="#fff" stroke-width="2.2"/></svg></div>
  <div class="feat right" style="top:290px"><h4>Quality/Integrity</h4><p>Equipment are regularly maintain and calibrated to meet.</p>
    <svg class="feat-icon" width="34" height="34" viewBox="0 0 34 34"><path d="M17 3l4 9 10 1-7 7 2 10-9-5-9 5 2-10-7-7 10-1z" fill="none" stroke="#fff" stroke-width="2.2"/></svg></div>
  <div class="feat right" style="top:400px"><h4>Experience</h4><p>With more than 20 years in the market, we know the.</p>
    <svg class="feat-icon" width="34" height="34" viewBox="0 0 34 34"><circle cx="13" cy="11" r="6" fill="none" stroke="#fff" stroke-width="2.2"/><path d="M2 30c0-7 5-11 11-11s11 4 11 11M24 6a5 5 0 010 10M26 20c4 1 7 5 7 10" fill="none" stroke="#fff" stroke-width="2.2"/></svg></div>
</section>

<section>
  <div class="sec-title" style="top:2856px">
    <h2>Our Products</h2>
    <p>Handling extensive range of products by our professional guarantee you to extract the best value for your materials.</p>
  </div>
  <div class="prod" style="left:20px">
    <div class="prod-photo" role="img" aria-label="Photo of stacked aluminium wheel rims" style="background:linear-gradient(160deg,#e9e9e9,#9fa2a6 50%,#4b4e52)"></div>
    <div class="cat">OTHER</div><h3>Aluminium Rim</h3><div class="price">SGD 1,800.00</div>
    <div class="cart"><svg width="18" height="16" viewBox="0 0 18 16"><path d="M1 2h3l2 9h9l2-7H5" fill="none" stroke="#fff" stroke-width="2"/></svg></div>
  </div>
  <div class="prod" style="left:352px">
    <div class="prod-photo" role="img" aria-label="Photo of baled radiator fins" style="background:linear-gradient(160deg,#d8d8d8,#8b8d90 50%,#505256)"></div>
    <div class="cat">OTHER</div><h3>Radiator Fins</h3><div class="price">SGD 1,500.00</div>
    <div class="cart"><svg width="18" height="16" viewBox="0 0 18 16"><path d="M1 2h3l2 9h9l2-7H5" fill="none" stroke="#fff" stroke-width="2"/></svg></div>
  </div>
  <div class="prod" style="left:680px">
    <div class="prod-photo" role="img" aria-label="Photo of bright copper wire scrap" style="background:linear-gradient(160deg,#f0b48a,#c9663a 50%,#7a2e1c)"></div>
    <div class="cat">OTHER</div><h3>Berry Candy (M)</h3><div class="price">SGD 5,000.00</div>
    <div class="cart"><svg width="18" height="16" viewBox="0 0 18 16"><path d="M1 2h3l2 9h9l2-7H5" fill="none" stroke="#fff" stroke-width="2"/></svg></div>
  </div>
  <div class="pager" style="top:3082px">NEXT ›</div>
  <div class="pager" style="top:3142px">‹ PREV</div>
</section>

<section class="cta">
  <h2>Have scrap? Get us to call you today!</h2>
  <p>Contact us to understand how we can be at your service.</p>
</section>

<footer class="footer">
  <div class="brand"><div class="brand-square"></div><div class="brand-name">KIAN HENG</div></div>
  <div class="socials"><i></i><i></i><i></i><i></i></div>
  <div class="fcol" style="left:432px"><h4>Quick Links</h4>Home<br>About Us<br>Product<br>Services<br>Investors<br>Contact Us</div>
  <div class="fcol" style="left:636px"><h4>Information</h4>Terms &amp; Condition<br>Privacy Policy<br>FAQ<br>Disclaimers<br>Reviews</div>
  <div class="fcol" style="left:864px"><h4>Kian Heng Recycling</h4>
    <div class="row"><svg width="14" height="14" viewBox="0 0 24 24"><path d="M6 3l4 4-2 3c1 3 3 5 6 6l3-2 4 4-3 3C9 21 3 15 3 6z" fill="var(--gold)"/></svg><div><b>Phone</b>+(65) 6000 1234</div></div>
    <div class="row"><svg width="14" height="14" viewBox="0 0 24 24"><path d="M2 5h20v14H2zM2 5l10 8 10-8" fill="none" stroke="var(--gold)" stroke-width="2.4"/></svg><div><b>Email</b>hello@kianheng.example</div></div>
    <div class="row"><svg width="14" height="14" viewBox="0 0 24 24"><path d="M12 2a7 7 0 00-7 7c0 5 7 13 7 13s7-8 7-13a7 7 0 00-7-7z" fill="var(--gold)"/><circle cx="12" cy="9" r="2.5" fill="var(--dark)"/></svg><div><b>Address</b>12 Harbour Works Road,<br>Singapore 700000</div></div>
  </div>
</footer>
<div class="abs btn-gold cta-btn">CONTACT US NOW
  <svg width="22" height="22" viewBox="0 0 22 22"><path d="M3 19L19 3M8 3h11v11" fill="none" stroke="#fff" stroke-width="2.4"/></svg>
</div>
<div class="footer-bar">Copyright © Kian Heng Recycling. All Rights Reserved.</div>
<div class="to-top"></div>

</body>
</html>
```